Business Card for beauty technology startup

Design Glowmi Business Card for a Beauty, based on the website identity and colors (https://www.glowmi-example.com).
Glowmi is a beauty tech startup that gathers helpful product info for beauty lovers and consumers (such as availability on stores, price range and product reviews) for makeup products. The card design must be young, colorful but clean, and very modern.

Target Market(s)

woman, 15-35

Industry/Entity Type

Cosmetics

Contact Information for Business Card

Full Name, address, phone

Font styles to use
Other font styles liked:
• Advent Pro

Colors
e34297
86cfc6
ffffff
5c5c5c
e8e8e8
e667a6
b2b2b2

Requirements
Must have
• One full colored side with a creative design and another with card info
• Use Color palette: #95C5C5 and/or #D38AA5
• Use fonts: Advent Pro
• Use website identity: https://www.glowmi-example.com
Nice to have
• If needed extra font: Roboto

```html
<!DOCTYPE html>
<html lang="en">
<head>
<meta charset="utf-8">
<title>Glowmi Business Card</title>
<link rel="stylesheet" href="https://fonts.googleapis.com/css2?family=Advent+Pro:wght@300;400&family=Roboto:wght@300;400;700&display=swap">
<style>
  :root {
    --backdrop: #ececec;
    --rose: #b27b95;
    --rose-deep: #a06a84;
    --rose-light: #e4bfd8;
    --paper: #ffffff;
    --stone: #c2c2c2;
    --ink-white: #ffffff;
  }
  * { margin: 0; padding: 0; box-sizing: border-box; }
  html, body {
    width: 1200px; height: 900px; overflow: hidden;
    background: var(--backdrop);
  }
  .canvas { position: relative; width: 1200px; height: 900px; }

  .card {
    position: absolute; left: 280px; width: 640px; height: 366px;
    overflow: hidden;
    box-shadow: 0 6px 18px rgba(0,0,0,0.12);
  }

  /* Front side */
  .card-front {
    top: 66px;
    background: linear-gradient(110deg, var(--rose-light) 0%, #c38ea9 45%, var(--rose-deep) 100%);
  }
  .front-mark {
    position: absolute; left: 0; right: 0; top: 92px;
    display: flex; flex-direction: column; align-items: center; gap: 22px;
  }
  .front-ring {
    width: 86px; height: 86px; border-radius: 50%;
    border: 3px solid var(--ink-white);
  }
  .front-name {
    font-family: "Advent Pro", sans-serif; font-weight: 300;
    font-size: 54px; letter-spacing: 12px; color: var(--ink-white);
    padding-left: 12px; line-height: 1;
  }

  /* Back side */
  .card-back { top: 468px; background: var(--paper); }
  .back-brand {
    position: absolute; left: 150px; top: 86px;
    display: flex; align-items: center; gap: 26px;
  }
  .back-ring {
    width: 78px; height: 78px; border-radius: 50%;
    border: 3px solid var(--rose);
    flex: none;
  }
  .back-name {
    font-family: "Advent Pro", sans-serif; font-weight: 300;
    font-size: 58px; letter-spacing: 11px; color: var(--rose);
    line-height: 1;
  }
  .info-band {
    position: absolute; left: 0; right: 0; top: 206px; height: 116px;
    background: var(--rose);
  }
  .footer-strip {
    position: absolute; left: 0; right: 0; bottom: 0; height: 44px;
    background: var(--stone);
  }
  .person {
    position: absolute; left: 26px; top: 238px;
    font-family: "Roboto", sans-serif; color: var(--ink-white);
    font-weight: 300; font-size: 14px; line-height: 18px;
  }
  .person-name { font-weight: 700; font-size: 14px; letter-spacing: 0.5px; }
  .contacts {
    position: absolute; right: 22px; top: 214px;
    list-style: none;
    font-family: "Roboto", sans-serif; font-weight: 300;
    font-size: 13px; line-height: 17px; color: var(--ink-white);
    text-align: right;
  }
  .contacts li { display: flex; justify-content: flex-end; align-items: center; gap: 8px; }
  .contacts svg { width: 11px; height: 11px; fill: var(--ink-white); }
  .web {
    position: absolute; right: 24px; top: 296px;
    font-family: "Roboto", sans-serif; font-weight: 400;
    font-size: 13px; letter-spacing: 7px; color: var(--ink-white);
  }
</style>
</head>
<body>
<main class="canvas">

  <section class="card card-front" aria-label="Card front">
    <div class="front-mark">
      <div class="front-ring"></div>
      <div class="front-name">GLOWMI</div>
    </div>
  </section>

  <section class="card card-back" aria-label="Card back">
    <div class="back-brand">
      <div class="back-ring"></div>
      <div class="back-name">GLOWMI</div>
    </div>

    <div class="info-band"></div>
    <div class="footer-strip"></div>

    <div class="person">
      <div class="person-name">MARA LINDQVIST</div>
      <div>CEO/FOUNDER</div>
      <div>214 Lilac Court</div>
      <div>Fairview, Oregon 97024</div>
    </div>

    <ul class="contacts">
      <li>555 014 2538
        <svg viewBox="0 0 12 12"><path d="M1 3 Q6 -1 11 3 L9 5 L7.5 4 L4.5 4 L3 5 Z M2 6 H10 V11 H2 Z"/></svg>
      </li>
      <li>555 018 9364
        <svg viewBox="0 0 12 12"><path d="M3 0 H9 V12 H3 Z M4 1.5 V9.5 H8 V1.5 Z" fill-rule="evenodd"/></svg>
      </li>
      <li>555 012 1940
        <svg viewBox="0 0 12 12"><path d="M3 0 H9 V4 H3 Z M0 5 H12 V10 H9 V12 H3 V10 H0 Z"/></svg>
      </li>
      <li>info@glowmi-example.com
        <svg viewBox="0 0 12 12"><path d="M0 2 H12 V10 H0 Z M1 3 L6 7 L11 3 Z" fill-rule="evenodd"/></svg>
      </li>
    </ul>

    <div class="web">www.glowmi-example.com</div>
  </section>

</main>
</body>
</html>
```